Auto Bodyshop Personal Injury Clients Focus

We are a busy body shop that focuses on personal injury work and custom work.

Please review website. We need marketing material. Outside of the basic body shop material we want to add a few points that make us stand out.

https://www.ratemyspot.example/biz/durvin-collision-los-angeles-2

https://www.snapgrid.example/durvincollision/

http://www.durvincollision.example/

Please gather material from our website. Stay consistent with color and modern design and incorporate with better working the following points.

1. Can pick up and tow cars from any geographic location
2. Provide rentals and will drop off and pick them up
3. Can work on a lien basis
4. Handle Property damage as a curtesy
5. have huge storage capabilities
6. Quick turn around on estimates
7. Offer Presentation Packages for litigation purposes.

I want to give designers more time

Attorneys

Personal Injury, Auto Body Shop

Must have
• Tri fold, double sided, USA letter format
Nice to have
• As much information as possible but on the front page the important points I added but maybe bettter more professional wording

```html
<!DOCTYPE html>
<html lang="en">
<head>
<meta charset="utf-8">
<title>Durvin Collision – Tri-fold Brochure</title>
<link href="https://fonts.googleapis.com/css2?family=Montserrat:wght@400;600;700;800&family=Open+Sans:ital,wght@0,400;0,600;1,400&display=swap" rel="stylesheet">
<style>
  :root{
    --ink:#1b1b1b;
    --ink-soft:#262626;
    --gold:#eaa623;
    --paper:#e9e9e9;
    --white:#ffffff;
    --text-light:#d8d8d8;
    --backdrop:#f2f2f2;
  }
  *{box-sizing:border-box;margin:0;padding:0}
  html,body{width:1200px;height:2399px;overflow:hidden;background:var(--backdrop)}
  body{position:relative;font-family:"Open Sans",Arial,sans-serif;color:var(--text-light)}
  .sheet{position:absolute;left:50px;width:1100px;height:850px;background:var(--ink);overflow:hidden;box-shadow:0 10px 30px rgba(0,0,0,.18)}
  .sheet--outside{top:190px}
  .sheet--inside{top:1300px}
  .sheet-art{position:absolute;inset:0;width:1100px;height:850px}
  .panel{position:absolute;top:0;width:366px;height:850px}
  .p1{left:0}.p2{left:367px}.p3{left:734px}
  .heading{font-family:"Montserrat",Arial,sans-serif;font-weight:800;text-transform:uppercase}
  .tab{position:absolute;background:var(--gold);color:var(--ink);font-family:"Montserrat",Arial,sans-serif;font-weight:800;text-transform:uppercase;padding:4px 26px 4px 14px;clip-path:polygon(0 0,100% 0,calc(100% - 14px) 100%,0 100%)}
  .body-copy{font-size:10.5px;line-height:1.45;color:var(--text-light)}
  .gold{color:var(--gold)}
  .brand{position:absolute;display:flex;align-items:center;gap:10px;font-family:"Montserrat",Arial,sans-serif;font-weight:800;color:var(--ink);text-transform:uppercase;letter-spacing:1px}
  .brand-dot{width:14px;height:14px;border-radius:50%;background:var(--ink)}

  /* outside */
  .about{position:absolute;left:30px;top:28px;width:310px}
  .about .tab{position:static;display:inline-block;font-size:13px;margin-bottom:10px}
  .about ul{list-style:none;margin-top:10px}
  .about li{font-size:11px;line-height:1.4;padding-left:18px;position:relative;margin-bottom:5px;font-style:italic}
  .about li::before{content:"";position:absolute;left:0;top:4px;width:8px;height:8px;border:1.5px solid var(--gold)}
  .estimate-band{left:0;top:598px;font-size:15px;padding:6px 40px 6px 52px}
  .rentals{position:absolute;left:30px;top:660px;width:300px;font-family:"Montserrat",Arial,sans-serif;font-weight:700;font-size:14px;line-height:1.35;text-transform:uppercase;color:var(--gold)}
  .litigation{position:absolute;left:50px;top:42px;width:270px;height:108px;border:2px solid var(--gold);border-radius:18px;background:rgba(0,0,0,.55);display:flex;align-items:center;justify-content:center;text-align:center;font-family:"Montserrat",Arial,sans-serif;font-weight:700;font-size:18px;line-height:1.3;color:var(--white)}
  .back-brand{left:60px;top:600px;font-size:20px}
  .contact{position:absolute;left:20px;top:680px;width:326px;text-align:center}
  .contact .label{font-family:"Montserrat",Arial,sans-serif;font-weight:800;font-size:13px;color:var(--gold);letter-spacing:1px}
  .icons{display:flex;justify-content:center;gap:12px;margin:8px 0}
  .icon{width:28px;height:28px;border-radius:50%;background:var(--gold);display:flex;align-items:center;justify-content:center}
  .phone{font-family:"Montserrat",Arial,sans-serif;font-weight:800;font-size:24px;color:var(--white)}
  .web-small{font-size:11px;margin-top:4px;color:var(--text-light)}
  .address{font-size:10.5px;margin-top:4px;color:var(--text-light)}
  .cover-brand{left:40px;top:560px;font-size:24px}
  .cover-tagline{position:absolute;left:34px;top:660px;width:300px;font-family:"Montserrat",Arial,sans-serif;font-weight:800;font-size:19px;line-height:1.3;text-transform:uppercase;color:var(--gold)}
  .cover-tagline .white{color:var(--white)}
  .cover-web{position:absolute;left:0;bottom:0;width:366px;height:44px;background:var(--gold);color:var(--ink);font-family:"Montserrat",Arial,sans-serif;font-weight:800;font-size:16px;display:flex;align-items:center;justify-content:flex-end;padding-right:30px;clip-path:polygon(40px 0,100% 0,100% 100%,0 100%)}

  /* inside */
  .workmanship{position:absolute;left:26px;top:26px;width:318px}
  .workmanship h2{font-size:26px;color:var(--white);margin-bottom:6px}
  .workmanship .tab{position:static;display:inline-block;font-size:12px;margin:10px 0 6px}
  .workmanship h3,.services-mid h3{font-family:"Montserrat",Arial,sans-serif;font-weight:700;font-size:13.5px;color:var(--gold);margin:12px 0 4px}
  .inside-estimate{left:0;bottom:32px;font-size:16px;padding:7px 44px 7px 28px}
  .services-mid{position:absolute;left:22px;top:250px;width:324px}
  .services-mid h3:first-child{margin-top:0}
  .consult-tab{position:absolute;left:20px;bottom:40px;background:var(--gold);color:var(--ink);padding:6px 30px 6px 18px;clip-path:polygon(12px 0,100% 0,calc(100% - 12px) 100%,0 100%);font-family:"Montserrat",Arial,sans-serif;font-weight:800}
  .consult-tab small{display:block;font-size:10px;letter-spacing:1px}
  .consult-tab strong{display:block;font-size:18px}
  .inside-web{position:absolute;right:0;bottom:26px;width:230px;height:34px;background:var(--white);color:var(--ink);font-family:"Montserrat",Arial,sans-serif;font-weight:700;font-size:12px;display:flex;align-items:center;justify-content:center;clip-path:polygon(24px 0,100% 0,100% 100%,0 100%)}
</style>
</head>
<body>

<!-- OUTSIDE OF BROCHURE -->
<section class="sheet sheet--outside" aria-label="Brochure outside">
  <svg class="sheet-art" viewBox="0 0 1100 850" aria-hidden="false">
    <rect width="1100" height="850" fill="#1b1b1b"/>
    <!-- collage band across first two panels -->
    <polygon role="img" aria-label="Photo of an orange classic car in the shop" points="0,330 150,320 200,470 0,480" fill="#8a6a3a"/>
    <polygon role="img" aria-label="Photo of a damaged white car" points="150,320 330,300 360,440 200,470" fill="#8e8e8e"/>
    <polygon role="img" aria-label="Photo of a red motorcycle under repair" points="0,480 200,470 260,580 0,590" fill="#9a2a2a"/>
    <polygon role="img" aria-label="Photo of a blue muscle car" points="200,470 360,440 440,560 260,580" fill="#2f3f8a"/>
    <polygon role="img" aria-label="Photo of cars parked in the service bay" points="330,300 520,280 560,420 360,440" fill="#6f6f6f"/>
    <polygon role="img" aria-label="Photo of a classic car interior" points="360,440 560,420 600,540 440,560" fill="#b7b7b7"/>
    <!-- black and white hot rod photo spanning middle and cover -->
    <polygon role="img" aria-label="Black and white photo of a vintage hot rod wheel" points="520,280 734,170 734,560 600,540 560,420" fill="#505050"/>
    <polygon role="img" aria-label="Black and white photo of a vintage hot rod wheel" points="734,0 1100,0 1100,520 734,560" fill="#4a4a4a"/>
    <!-- light brand areas -->
    <polygon points="367,580 600,545 733,575 733,660 367,670" fill="#e9e9e9"/>
    <polygon points="734,560 1100,520 1100,640 760,650 734,640" fill="#e9e9e9"/>
    <!-- gold trims -->
    <polygon points="0,590 260,580 600,545 600,552 260,588 0,598" fill="#eaa623"/>
    <rect x="0" y="832" width="734" height="18" fill="#eaa623"/>
    <line x1="366.5" y1="0" x2="366.5" y2="850" stroke="#000" stroke-opacity=".35"/>
    <line x1="733.5" y1="0" x2="733.5" y2="850" stroke="#000" stroke-opacity=".35"/>
  </svg>

  <div class="panel p1">
    <div class="about">
      <span class="tab">About Us</span>
      <p class="body-copy" style="font-style:italic">Durvin Collision has a long history of serving the Sun Valley, North Hollywood, Sunland, Arleta, Valley Glen, Valley Village and Burbank communities.</p>
      <ul>
        <li>Can work on a lien basis</li>
        <li>Handle property damage as a courtesy</li>
        <li>Have huge storage capabilities</li>
        <li>Quick turn around on estimates</li>
      </ul>
    </div>
    <div class="tab estimate-band">Get an Estimate</div>
    <p class="rentals">Provide rentals and will<br>drop off &amp; pick them up</p>
  </div>

  <div class="panel p2">
    <div class="litigation">Offer Presentation<br>Packages for<br>litigation purposes.</div>
    <div class="brand back-brand"><span class="brand-dot"></span>Durvin Collision</div>
    <div class="contact">
      <div class="label">FREE CONSULTATIONS</div>
      <div class="icons">
        <span class="icon"><svg width="14" height="14" viewBox="0 0 24 24"><path d="M6.6 10.8a15 15 0 0 0 6.6 6.6l2.2-2.2c.3-.3.7-.4 1-.2 1.1.4 2.3.6 3.6.6.6 0 1 .4 1 1V20c0 .6-.4 1-1 1A17 17 0 0 1 3 4c0-.6.4-1 1-1h3.5c.6 0 1 .4 1 1 0 1.3.2 2.5.6 3.6.1.3 0 .7-.2 1z" fill="#1b1b1b"/></svg></span>
        <span class="icon"><svg width="14" height="14" viewBox="0 0 24 24"><circle cx="12" cy="12" r="9" fill="none" stroke="#1b1b1b" stroke-width="2"/><path d="M3 12h18M12 3c3 3 3 15 0 18M12 3c-3 3-3 15 0 18" fill="none" stroke="#1b1b1b" stroke-width="1.6"/></svg></span>
        <span class="icon"><svg width="14" height="14" viewBox="0 0 24 24"><path d="M12 2a7 7 0 0 0-7 7c0 5 7 13 7 13s7-8 7-13a7 7 0 0 0-7-7zm0 9.5A2.5 2.5 0 1 1 12 6.5a2.5 2.5 0 0 1 0 5z" fill="#1b1b1b"/></svg></span>
      </div>
      <div class="phone">+1 818-555-0147</div>
      <div class="web-small">www.durvincollision.example</div>
      <div class="address">2250 Halvern Ave, Sun Valley, CA 91352, USA</div>
    </div>
  </div>

  <div class="panel p3">
    <div class="brand cover-brand"><span class="brand-dot"></span>Durvin Collision</div>
    <p class="cover-tagline">Can pick up and tow<br><span class="white">cars from any</span><br>geographic location</p>
    <div class="cover-web">durvincollision.example</div>
  </div>
</section>

<!-- INSIDE OF BROCHURE -->
<section class="sheet sheet--inside" aria-label="Brochure inside">
  <svg class="sheet-art" viewBox="0 0 1100 850">
    <rect width="1100" height="850" fill="#1b1b1b"/>
    <polygon role="img" aria-label="Photo of a rusty orange classic beetle" points="367,0 734,0 734,200 367,235" fill="#b8621e"/>
    <polygon role="img" aria-label="Photo of a technician grinding a red car panel" points="790,80 1070,40 1070,300 790,330" fill="#c23a4a"/>
    <polygon role="img" aria-label="Photo of a white car in the shop" points="1010,320 1100,310 1100,560 1010,570" fill="#7a7a7a"/>
    <polygon role="img" aria-label="Photo of a restored red classic car" points="790,350 1000,325 1000,740 790,760" fill="#8a3a2a"/>
    <rect x="0" y="835" width="1100" height="15" fill="#eaa623"/>
    <line x1="366.5" y1="0" x2="366.5" y2="850" stroke="#000" stroke-opacity=".35"/>
    <line x1="733.5" y1="0" x2="733.5" y2="850" stroke="#000" stroke-opacity=".35"/>
  </svg>

  <div class="panel p1">
    <div class="workmanship">
      <h2 class="heading">Workmanship</h2>
      <p class="body-copy">Our collision repair team is equipped and trained to bring your vehicle back to industry standards and back to life. Durvin Collision provides a lifetime warranty on all repairs completed at our shop. The auto body repair process is changing every day and you need a team with experience and manufacturer repair know how to put your car back on the road safely. Please review our before and after photos.</p>
      <span class="tab">Services</span>
      <p class="body-copy">Durvin Collision provides a multitude of services: auto body and collision repair, frame and unibody diagnosis, repair and replacement, aluminum and composite body type repair, vehicle customization and classic car restoration, from classic to contemporary to exotic vehicles, we can do it all.</p>
      <h3>Aluminum and Composite body type repair:</h3>
      <p class="body-copy">The best part about Durvin Collision is that with our training and equipment, we have the know how to repair and replace today's complicated auto body structures. Vehicles are constructed with different metal configurations to make them lighter, which in turn makes them more fuel efficient. Composite materials and plastics also make a difference in fuel efficiency. Our technicians are trained and ready to handle all collision repair needs.</p>
      <h3>Vehicle Customization:</h3>
      <p class="body-copy">The best part about Durvin Collision is that our team fully understands your desires when it comes to a customized vehicle. Customization is one of many services we provide for our customers. The entire team is ready to work diligently and make your dream custom car a reality. Just meet with us once and you won't be disappointed.</p>
    </div>
    <div class="tab inside-estimate">Get an Estimate</div>
  </div>

  <div class="panel p2">
    <div class="services-mid">
      <h3>Frame and Unibody Repair:</h3>
      <p class="body-copy">Durvin Collision is equipped with modern frame and unibody diagnosis and repair systems. Our shop has an impressive track record in fixing and repairing all makes and models. <span class="gold">Contact us to get a free estimate today!</span></p>
      <h3>Classic Car Restoration:</h3>
      <p class="body-copy">The more classic it gets, the tougher it is to restore. We absolutely understand what a prized possession a classic car must be, and we put our top technicians to work for you. Our team believes in your classic car project and will help you accomplish your restoration dreams. We have world class machinery to diagnose and build a classic car for our clients. It takes time because it's not just a car, it is a piece of art. Contact our customer service team for more details.</p>
      <h3>Auto Body / Collision Repair:</h3>
      <p class="body-copy">Auto body repair and collision damage diagnosis and repair are changing day by day. Vehicles have a vast array of electronics, safety systems and lighter but stronger body structures. Your vehicle needs an auto body shop that understands these new technologies and can repair them.</p>
    </div>
    <div class="consult-tab"><small>FREE CONSULTATIONS</small><strong>+1 818-555-0147</strong></div>
  </div>

  <div class="panel p3">
    <div class="inside-web">www.durvincollision.example</div>
  </div>
</section>

</body>
</html>
```